Simplified minimalist but bold website

Design a website for a brand 'Gather Every Moment' that shares ideas to make managing home and health easier through email swap series, webinars and eventually courses.

Simple landing page to attract users to sign up for a freebie.

Target Market(s)

women with families & homes to run

Number of Pages Required

1 page

Font styles to use
Sans Serif

Colors
e667a6
b768aa
acd136
ffffff
959595

Requirements
Must have
• Simplified look, line icons, opt-in template, contact us form

```html
<!DOCTYPE html>
<html lang="en">
<head>
<meta charset="utf-8">
<title>Gather Every Moment</title>
<link href="https://fonts.googleapis.com/css2?family=Open+Sans:wght@300;400;600;700&display=swap" rel="stylesheet">
<style>
:root{
  --pink:#e667a6;
  --purple:#b768aa;
  --green:#acd136;
  --blue:#35a7d8;
  --grey:#959595;
  --ink:#222;
  --page:#e6e6e6;
  --panel:#d6d6d6;
  --band:#ececec;
  --white:#ffffff;
}
*{box-sizing:border-box;margin:0;padding:0}
html,body{width:1200px;height:1200px;overflow:hidden;background:var(--page);font-family:"Open Sans",sans-serif;color:var(--ink)}
.site{position:absolute;left:369.6px;top:0;width:576px;height:1500px;background:var(--white);transform:scale(.8);transform-origin:0 0;overflow:hidden}
.abs{position:absolute}
.header{left:0;top:0;width:576px;height:40px;background:var(--white)}
.brand{left:63px;top:11px;font-size:13px;color:var(--pink);font-weight:400}
.nav{right:60px;top:15px;display:flex;gap:11px;font-size:8px;font-weight:600;letter-spacing:.3px}
.hero{left:0;top:40px;width:576px;height:277px;border:1px solid #bfe0f0;overflow:hidden}
.hero svg{position:absolute;left:0;top:0}
.hero-title{left:46px;top:68px;width:200px;text-align:center;color:var(--pink);font-size:8.5px;font-weight:600}
.hero-sub{left:46px;top:99px;width:200px;text-align:center;font-size:8px;font-weight:600;line-height:10px}
.hero-arrow{left:136px;top:144px}
.kicker{font-size:9px;color:#444}
.section-title{font-size:13px;color:#333}
.rule{height:2px;background:var(--purple)}
.lede{font-size:12px;line-height:15px;color:#111}
.small{font-size:7.5px;line-height:9.6px;color:#111}
.btn{display:flex;align-items:center;justify-content:center;color:var(--white);font-size:6.5px;font-weight:700}
.btn.green{background:var(--green)}
.btn.blue{background:var(--blue)}
.field{background:var(--white);font-size:6.5px;font-weight:600;padding:6px 5px;height:21px}
.field.dim{background:var(--panel)}
.band{left:0;top:652px;width:576px;height:275px;background:var(--band)}
.center{text-align:center}
.copy{font-size:9.5px;line-height:12px;color:#111}
.services{left:0;top:1182px;width:576px;height:266px}
.plan{background:#d9d9d9;width:106px;height:142px}
.plan.feature{background:#c6c6c6}
.plan .term{position:absolute;top:4px;left:0;width:100%;text-align:center;font-size:8.5px}
.plan .term span{display:inline-block;border-bottom:1.5px solid var(--purple);padding:0 4px 1px}
.plan .sess{position:absolute;top:24px;width:100%;text-align:center;font-size:8.5px}
.plan .price{position:absolute;top:52px;width:100%;text-align:center;font-size:30px;font-weight:300;color:#c889b9}
.plan .go{position:absolute;bottom:0;left:0;width:100%;height:19px;font-size:8.5px;font-weight:400}
.contact{font-size:9px;font-weight:700;color:#111;display:flex;align-items:center;gap:5px}
.footer{left:0;top:1448px;width:576px;height:52px;background:var(--blue);color:var(--white);font-size:6.5px;font-weight:700}
</style>
</head>
<body>
<div class="site">

  <header class="abs header">
    <div class="abs brand">Gather Every Moment</div>
    <nav class="abs nav"><span>HOME</span><span>ABOUT</span><span>BLOG</span><span>CONTACT</span></nav>
  </header>

  <section class="abs hero">
    <svg width="576" height="277" viewBox="0 0 576 277">
      <path d="M223 0 C 330 60, 330 200, 272 277 L576 277 L576 0 Z" fill="var(--blue)"/>
      <rect x="228" y="20" width="250" height="230" fill="#3a9fd0" role="img" aria-label="Illustration of two people arranging sticky notes on a planning board"/>
    </svg>
    <div class="abs hero-title">Gather Every Moment.</div>
    <div class="abs hero-sub">Chances are life is a little overwhelming.<br>Let us help</div>
    <svg class="abs hero-arrow" width="14" height="14" viewBox="0 0 14 14">
      <circle cx="7" cy="7" r="7" fill="#777"/>
      <path d="M7 3.5 V10 M4 7.2 L7 10 L10 7.2" stroke="#fff" stroke-width="1.6" fill="none"/>
    </svg>
  </section>

  <div class="abs kicker" style="left:62px;top:345px">Baby Steps... (try out a few of our tricks)</div>

  <div class="abs section-title" style="left:62px;top:399px">Swaps Email Series</div>
  <div class="abs rule" style="left:62px;top:423px;width:78px"></div>
  <div class="abs lede" style="left:63px;top:447px">Save TIME, MONEY and SANITY<br>with simple product swaps.</div>
  <div class="abs small" style="left:62px;top:501px;width:190px">Reduce the amount of work it takes to run your home.<br>Swap out existing products for more convenient ones.<br>Each swap saves you work, clutter, time &amp; money.</div>
  <div class="abs btn green" style="left:62px;top:599px;width:67px;height:23px">See SampleSwap</div>
  <div class="abs btn blue" style="left:141px;top:599px;width:67px;height:23px">Learn More</div>

  <form class="abs" style="left:293px;top:401px;width:220px;height:221px;background:var(--panel)">
    <div class="abs field" style="left:28px;top:58px;width:163px">Name</div>
    <div class="abs field" style="left:28px;top:96px;width:163px">Email</div>
    <div class="abs btn green" style="left:28px;top:140px;width:163px;height:24px">SIGN ME UP</div>
  </form>

  <section class="abs band">
    <div class="abs kicker" style="left:62px;top:43px">Big Leap... (I'm ready to roll up my sleeves)</div>
    <div class="abs" style="left:62px;top:66px;width:182px;text-align:center;font-size:10.5px">Decluttering Guide</div>
    <div class="abs" role="img" aria-label="Printed decluttering guide pages" style="left:72px;top:112px;width:160px;height:128px;background:linear-gradient(135deg,#f4f4f4,#e2e2e2)"></div>
    <form class="abs" style="left:293px;top:22px;width:220px;height:222px;background:#f5f5fa">
      <div class="abs center" style="left:0;top:38px;width:220px;font-size:8.5px;font-weight:600">Declutter your home</div>
      <div class="abs field dim" style="left:28px;top:71px;width:163px">Name</div>
      <div class="abs field dim" style="left:28px;top:108px;width:163px">Email</div>
      <div class="abs btn green" style="left:28px;top:152px;width:163px;height:23px">SEND ME THE GUIDE</div>
    </form>
  </section>

  <div class="abs section-title center" style="left:0;top:941px;width:576px;font-size:11.5px">Swaps Email Series</div>
  <div class="abs rule" style="left:246px;top:962px;width:86px"></div>
  <div class="abs copy center" style="left:0;top:992px;width:576px">Save TIME, MONEY and SANITY with simple product swaps.<br>And reduce the amount of work it takes to run your home.<br>Swap out existing products for more convenient ones.<br>Each swap save you work, clutter, time &amp; money.<br>You get an email 2x weekly for 6-12 weeks only<br>Get even more if you feel they are helpful to you</div>
  <div class="abs copy center" style="left:0;top:1076px;width:576px">Join our monthly SIMPLE SWAP SHARING web jams with other<br>mums and get even more ideas.<br>Better yet, come with great tips of your own to share.</div>
  <div class="abs btn green" style="left:216px;top:1136px;width:150px;height:23px;font-size:9px;font-weight:400">SIGN ME UP</div>

  <section class="abs services" role="img" aria-label="Softly faded photo of clothes hanging on a rail" style="background:linear-gradient(180deg,#a9a7a6 0%,#b3b4b8 45%,#c3c6cf 100%)">
    <div class="abs center" style="left:0;top:14px;width:576px;font-size:12px;color:#111">Organizing Services</div>
    <div class="abs rule" style="left:248px;top:32px;width:80px;height:1.5px"></div>

    <div class="abs plan" style="left:77px;top:60px">
      <div class="term" style="text-align:left;padding-left:26px"><span>First 1 Hour</span></div>
      <div class="price">$50</div>
      <div class="go btn blue">SIGN UP</div>
    </div>
    <div class="abs plan feature" style="left:185px;top:60px">
      <div class="term"><span>1 Hour</span></div>
      <div class="price">$75</div>
      <div class="go btn green">SIGN UP</div>
    </div>
    <div class="abs plan" style="left:292px;top:60px">
      <div class="term"><span>3 Hours</span></div>
      <div class="sess">1 Session</div>
      <div class="price">$200</div>
      <div class="go btn blue">SIGN UP</div>
    </div>
    <div class="abs plan" style="left:399px;top:60px;width:105px">
      <div class="term"><span>5 Hours</span></div>
      <div class="sess">1 - 2 Sessions</div>
      <div class="price">$300</div>
      <div class="go btn blue">SIGN UP</div>
    </div>

    <div class="abs contact" style="left:61px;top:234px">Contact Info:</div>
    <div class="abs contact" style="left:240px;top:234px">
      <svg width="11" height="11" viewBox="0 0 24 24"><path d="M6.6 10.8a15 15 0 0 0 6.6 6.6l2.2-2.2a1 1 0 0 1 1-.25 11.4 11.4 0 0 0 3.6.57 1 1 0 0 1 1 1V20a1 1 0 0 1-1 1A17 17 0 0 1 3 4a1 1 0 0 1 1-1h3.5a1 1 0 0 1 1 1c0 1.25.2 2.45.57 3.6a1 1 0 0 1-.25 1z" fill="#111"/></svg>
      555.014.2290
    </div>
    <div class="abs contact" style="left:394px;top:232px">
      <svg width="13" height="10" viewBox="0 0 13 10"><rect x=".5" y=".5" width="12" height="9" fill="none" stroke="#111"/><path d="M.5 .5 L6.5 5.5 L12.5 .5 M.5 9.5 L5 4.5 M12.5 9.5 L8 4.5" fill="none" stroke="#111"/></svg>
      hello@gathermoment.net
    </div>
  </section>

  <footer class="abs footer">
    <nav class="abs" style="left:63px;top:24px;display:flex;gap:9px"><span>HOME</span><span>ABOUT</span><span>BLOG</span><span>CONTACT</span></nav>
    <div class="abs" style="right:62px;top:24px">Copy Right@2018 All Rights Reserved</div>
  </footer>

</div>
</body>
</html>
```